Amberline Picture Works Web Design

COMPANY: AMBERLINE PICTURE WORKS
LOCATION: SHANGHAI, CHINA
AREA: FILM/TV DRAMA/COMMERCIALS/GAME POST PRODUCTION, SOUND DESIGN, MUSIC, and GAME.
WEB STYLE: SIMPLE, PROFESSIONAL, TRUSTWORTHY

LANGUAGE: ENGLISH, CHINESE. (Same layout, different language)
UPDATE: AFTER PROJECT FINISHED, WE NEED UPDATE BY OURSELVES.

MAIN SUBJECT: 6
1 HOMEPAGE
2 ABOUT US
3 TEAM
4 SERVICES
5 FACILITY
6 CONTACT

add one page of JOB OPPORTUNITIES.

DETAILS
1 HOMEPAGE
SLOGAN: Amberline Picture Works provides a well-designed working environment which amplifies your team’s ability to reach their creative goals.

Our services include:
 Feature Films
 Music & Scoring
 Commercials
 ADR & Foley
 Sound & Picture Editorial
 Sound Design
 Video Game

2 ABOUT US
Amberline Picture Works is located in the premiere South-Bund area of Shanghai. Occupying a 5000 square meter Technical Building, Amberline Picture Works was built by a filmmaker for filmmakers, and is one of the largest, most versatile full-service post-production facilities in China.

Amberline Picture Works is positioning to be at the forefront of the latest technology. Our goal is to provide a comprehensive solution for the post-production needs of our clients. We offer two fully-equipped dubbing stages (one of which will be certified VORTAN SPHERA ELITE), a large variety of both picture and sound editing rooms, impressive Foley and ADR stages, a world-class scoring stage, and complete audio and video transfer services.

We can handle your entire project from editing all the way to the end of the final sound mix; all under one extremely comfortable roof. We fully realize that the true art is in listening to the needs of our clients and making their greatest vision a reality. To this end our creative team's expertise, with a network of sound supervisors, editors and mixers, will deliver the magic you need. Producers and directors will also find our richly appointed guest accommodations to be a comfortable and soothing place to wind up the day. Every aspect of your project will be taken care of by a skilled and dedicated team, in the way that is best suited to you.

3 TEAM
(attachment 01)

4 SERVICES
Sound Mix
ADR
FOLEY
MUSIC
Sound Design
Sound Edit
Picture Edit
for all the Films, TV Drama, Commercials, Video Games, Online Media
(attachment 02, use photo)

5 FACILITY
(attachment 03)

6 CONTACT
(attachment04)
with map

Reason: Designers work are great, my bosses will spend 1-2 days select one of these web design, and spend 1-2 days to make some change, maybe use new photos.

```html
<!DOCTYPE html>
<html lang="en">
<head>
<meta charset="utf-8">
<title>Amberline Picture Works</title>
<link rel="stylesheet" href="https://fonts.googleapis.com/css2?family=Bebas+Neue&family=Oswald:wght@500&family=Raleway:wght@300;400&display=swap">
<style>
  :root{
    --navy:#1b3a78;
    --navy-deep:#17306a;
    --ink:#1a2755;
    --sky:#7fa5f2;
    --muted:#5a6382;
    --soft:#9aa6c4;
    --panel:#f1f1f2;
    --white:#ffffff;
    --lang-active:#1f3f86;
    --lang-idle:#555a63;
  }
  *{box-sizing:border-box;margin:0;padding:0}
  html,body{width:713px;height:1200px;overflow:hidden;background:var(--white)}
  body{position:relative;font-family:"Raleway",sans-serif}

  /* Hero */
  .hero{position:absolute;left:0;top:0;width:713px;height:413px;
    background:radial-gradient(ellipse at 30% 40%,#6b5a48 0%,#3a2f27 45%,#17120f 100%)}
  .brand{position:absolute;left:306px;top:88px;width:100px;text-align:center;
    font-family:"Bebas Neue",sans-serif;font-size:22px;line-height:21px;color:var(--white);letter-spacing:1px}
  .lang{position:absolute;right:0;top:44px;width:25px}
  .lang span{display:block;height:24px;line-height:24px;text-align:center;color:var(--white);
    font-family:"Oswald",sans-serif;font-size:9px}
  .lang .on{background:var(--lang-active)}
  .lang .off{background:var(--lang-idle)}
  .slogan{position:absolute;left:116px;top:241px;width:510px;height:106px;background:rgba(20,18,18,.55);
    text-align:center;font-family:"Bebas Neue",sans-serif;color:var(--white)}
  .slogan .lead{font-size:17px;margin-top:14px;letter-spacing:.5px}
  .slogan .key{font-size:31px;color:var(--sky);line-height:32px;letter-spacing:.5px}
  .slogan .tail{font-size:17px;letter-spacing:.3px}
  .scroll{position:absolute;left:68px;top:376px;width:44px;text-align:center;
    font-family:"Oswald",sans-serif;font-size:7px;color:var(--white)}

  /* Nav */
  .nav{position:absolute;left:0;top:413px;width:713px;height:29px;background:var(--navy);
    display:flex;justify-content:center;gap:20px;align-items:center}
  .nav a{font-family:"Oswald",sans-serif;font-size:9px;color:var(--white);text-decoration:none;letter-spacing:.3px}

  /* Services band */
  .band{position:absolute;left:0;top:442px;width:713px;height:78px;
    background:linear-gradient(90deg,#3a0b10 0%,#6a1720 18%,#2a1a1a 24%,#1b1616 50%,#2a1a1a 76%,#6a1720 82%,#3a0b10 100%)}
  .band h2{position:absolute;left:0;right:0;top:28px;text-align:center;
    font-family:"Bebas Neue",sans-serif;font-weight:400;font-size:24px;color:var(--white);letter-spacing:.5px}

  /* Service grid */
  .grid{position:absolute;left:70px;top:520px;width:572px;height:572px;
    display:grid;grid-template-columns:286px 286px;grid-template-rows:190px 193px 189px}
  .photo{position:relative}
  .photo.rack{background:linear-gradient(135deg,#d9d4c9,#a39c90 55%,#3f3a35)}
  .photo.console{background:radial-gradient(ellipse at 50% 55%,#5f6a52,#2d332c 60%,#141614)}
  .photo.theatre{background:linear-gradient(90deg,#a1111c 0%,#c21a24 16%,#2b2624 22%,#4a433c 50%,#2b2624 78%,#c21a24 84%,#a1111c 100%)}
  .arrow{position:absolute;top:50%;margin-top:-11px}
  .arrow.prev{left:9px}
  .arrow.next{right:9px}
  .dots{position:absolute;bottom:6px;left:0;right:0;display:flex;justify-content:center;gap:4px}
  .dots i{width:5px;height:5px;border-radius:50%;background:var(--white)}
  .dots i.on{background:#9fb0cc}

  .text{padding:10px 14px 0 11px;position:relative;background:var(--white)}
  .text.alt{background:var(--panel)}
  .text h3{font-family:"Bebas Neue",sans-serif;font-weight:400;font-size:35px;line-height:34px;color:var(--ink);letter-spacing:.5px}
  .text h3 small{font-family:"Raleway",sans-serif;font-weight:300;font-size:20px;color:#8a8d96;margin-left:10px;letter-spacing:0}
  .text .rule{width:40px;height:3px;background:var(--navy);margin:5px 0 10px}
  .text p{font-family:"Raleway",sans-serif;font-size:9.2px;line-height:15px;text-transform:uppercase;color:var(--muted);width:262px}
  .more{display:inline-block;margin-top:10px;border:2px solid var(--ink);padding:4px 7px;
    font-family:"Bebas Neue",sans-serif;font-size:12px;color:var(--ink);letter-spacing:.3px;text-decoration:none}
  .text .icon{position:absolute;right:12px;top:12px}

  /* Footer */
  .footer{position:absolute;left:0;top:1092px;width:713px;height:108px;background:var(--navy-deep);text-align:center}
  .footer .icons{display:flex;justify-content:center;gap:18px;margin-top:18px;align-items:center}
  .footer .contact{margin-top:12px;font-family:"Bebas Neue",sans-serif;font-size:12px;color:var(--white);letter-spacing:.3px}
  .footer .contact b{font-weight:400;color:var(--sky);margin-left:10px}
  .footer .rule{width:340px;height:1px;background:#2e4a8a;margin:8px auto 6px}
  .footer .copy{font-family:"Raleway",sans-serif;font-size:6.5px;color:#6f82b4;text-transform:uppercase}
</style>
</head>
<body>

<header class="hero" role="img" aria-label="Close-up of a studio monitor speaker in a mixing room">
  <div class="brand">Amberline Picture Works</div>
  <div class="lang"><span class="on">EN</span><span class="off">CH</span></div>
  <div class="slogan">
    <div class="lead">Amberline Picture Works provides a</div>
    <div class="key">Well-designed working environment</div>
    <div class="tail">which amplifies your team's ability to reach their creative goals</div>
  </div>
  <div class="scroll">
    <svg width="14" height="20" viewBox="0 0 14 20"><rect x="1" y="1" width="12" height="18" rx="6" fill="#d9d9d9"/><rect x="6" y="4" width="2" height="5" rx="1" fill="#555"/></svg>
    <div>SCROLL DOWN</div>
  </div>
</header>

<nav class="nav">
  <a href="#">HOME</a><a href="#">ABOUT US</a><a href="#">TEAM</a><a href="#">SERVICES</a><a href="#">FACILITY</a><a href="#">CONTACT</a>
</nav>

<section class="band" role="img" aria-label="Screening room with red curtains">
  <h2>Our services include</h2>
</section>

<main class="grid">
  <div class="photo rack" role="img" aria-label="Rack-mounted audio processing equipment">
    <svg class="arrow prev" width="22" height="22" viewBox="0 0 22 22"><circle cx="11" cy="11" r="10" fill="none" stroke="#fff" stroke-width="1.2"/><path d="M13 6l-5 5 5 5" fill="none" stroke="#fff" stroke-width="1.4"/></svg>
    <svg class="arrow next" width="22" height="22" viewBox="0 0 22 22"><circle cx="11" cy="11" r="10" fill="none" stroke="#fff" stroke-width="1.2"/><path d="M9 6l5 5-5 5" fill="none" stroke="#fff" stroke-width="1.4"/></svg>
    <div class="dots"><i></i><i class="on"></i><i></i><i></i></div>
  </div>
  <div class="text">
    <h3>Feature<small>Films</small></h3>
    <div class="rule"></div>
    <p>Lorem Ipsum is simply dummy text of the printing and typesetting industry. Lorem Ipsum has been the industry's standard dummy text ever since the 1500s, when an unknown printer took a galley of type and scrambled it. Specimen book.</p>
    <a class="more" href="#">Click here for more</a>
    <svg class="icon" width="44" height="36" viewBox="0 0 44 36"><rect x="1" y="1" width="42" height="34" fill="none" stroke="#1b3a78" stroke-width="2"/><rect x="7" y="7" width="14" height="22" fill="#1b3a78"/><rect x="23" y="7" width="14" height="22" fill="#1b3a78"/><g fill="#1b3a78"><rect x="3" y="3" width="2" height="3"/><rect x="3" y="30" width="2" height="3"/><rect x="39" y="3" width="2" height="3"/><rect x="39" y="30" width="2" height="3"/></g></svg>
  </div>

  <div class="text alt">
    <h3>Music<small>&amp; Scoring</small></h3>
    <div class="rule"></div>
    <p>Lorem Ipsum is simply dummy text of the printing and typesetting industry. Lorem Ipsum has been the industry's standard dummy text ever since the 1500s, when an unknown printer took a galley of type and scrambled it. Specimen book.</p>
    <a class="more" href="#">Click here for more</a>
    <svg class="icon" width="34" height="38" viewBox="0 0 34 38"><path d="M10 8l22-6v26" fill="none" stroke="#1b3a78" stroke-width="3"/><path d="M10 8v24" stroke="#1b3a78" stroke-width="3"/><ellipse cx="6" cy="32" rx="6" ry="4.5" fill="#1b3a78"/><ellipse cx="28" cy="28" rx="6" ry="4.5" fill="#1b3a78"/></svg>
  </div>
  <div class="photo console" role="img" aria-label="Illuminated mixing console faders">
    <svg class="arrow prev" width="22" height="22" viewBox="0 0 22 22"><circle cx="11" cy="11" r="10" fill="none" stroke="#fff" stroke-width="1.2"/><path d="M13 6l-5 5 5 5" fill="none" stroke="#fff" stroke-width="1.4"/></svg>
    <svg class="arrow next" width="22" height="22" viewBox="0 0 22 22"><circle cx="11" cy="11" r="10" fill="none" stroke="#fff" stroke-width="1.2"/><path d="M9 6l5 5-5 5" fill="none" stroke="#fff" stroke-width="1.4"/></svg>
    <div class="dots"><i></i><i class="on"></i><i></i><i></i></div>
  </div>

  <div class="photo theatre" role="img" aria-label="Dubbing stage with screen and red wall panels">
    <svg class="arrow prev" width="22" height="22" viewBox="0 0 22 22"><circle cx="11" cy="11" r="10" fill="none" stroke="#fff" stroke-width="1.2"/><path d="M13 6l-5 5 5 5" fill="none" stroke="#fff" stroke-width="1.4"/></svg>
    <svg class="arrow next" width="22" height="22" viewBox="0 0 22 22"><circle cx="11" cy="11" r="10" fill="none" stroke="#fff" stroke-width="1.2"/><path d="M9 6l5 5-5 5" fill="none" stroke="#fff" stroke-width="1.4"/></svg>
    <div class="dots"><i></i><i class="on"></i><i></i><i></i></div>
  </div>
  <div class="text">
    <h3>Commercials</h3>
    <div class="rule"></div>
    <p>Lorem Ipsum is simply dummy text of the printing and typesetting industry. Lorem Ipsum has been the industry's standard dummy text ever since the 1500s, when an unknown printer took a galley of type and scrambled it. Specimen book.</p>
    <a class="more" href="#">Click here for more</a>
    <svg class="icon" width="38" height="38" viewBox="0 0 38 38"><path d="M12 2l7 8 7-8" fill="none" stroke="#1b3a78" stroke-width="2"/><rect x="1" y="10" width="36" height="26" rx="3" fill="#1b3a78"/><rect x="5" y="14" width="22" height="18" rx="2" fill="#fff"/><circle cx="32" cy="18" r="2" fill="#fff"/><circle cx="32" cy="25" r="2" fill="#fff"/></svg>
  </div>
</main>

<footer class="footer">
  <div class="icons">
    <svg width="20" height="20" viewBox="0 0 20 20"><rect x="2" y="13" width="16" height="6" fill="#3e5a98"/><rect x="9" y="4" width="2" height="10" fill="#3e5a98"/><circle cx="10" cy="4" r="3" fill="#3e5a98"/></svg>
    <svg width="18" height="20" viewBox="0 0 18 20"><path d="M6 4l10-3v13" fill="none" stroke="#3e5a98" stroke-width="2"/><path d="M6 4v12" stroke="#3e5a98" stroke-width="2"/><ellipse cx="3.5" cy="16" rx="3.5" ry="2.5" fill="#3e5a98"/><ellipse cx="13.5" cy="14" rx="3.5" ry="2.5" fill="#3e5a98"/></svg>
    <svg width="22" height="18" viewBox="0 0 22 18"><rect x="1" y="1" width="20" height="16" fill="none" stroke="#3e5a98" stroke-width="1.5"/><rect x="4" y="4" width="6" height="10" fill="#3e5a98"/><rect x="12" y="4" width="6" height="10" fill="#3e5a98"/></svg>
    <svg width="22" height="20" viewBox="0 0 22 20"><g stroke="#3e5a98" stroke-width="1.5"><path d="M3 1v18M8 1v18M13 1v18M18 1v18"/></g><g fill="#3e5a98"><rect x="1" y="5" width="4" height="3"/><rect x="6" y="12" width="4" height="3"/><rect x="11" y="7" width="4" height="3"/><rect x="16" y="13" width="4" height="3"/></g></svg>
    <svg width="22" height="22" viewBox="0 0 22 22"><path d="M7 1l4 5 4-5" fill="none" stroke="#3e5a98" stroke-width="1.5"/><rect x="1" y="6" width="20" height="15" rx="2" fill="#3e5a98"/><rect x="4" y="9" width="12" height="9" fill="#17306a"/></svg>
    <svg width="22" height="20" viewBox="0 0 22 20"><path d="M1 7h5l6-5v16l-6-5H1z" fill="#3e5a98"/><path d="M15 6q3 4 0 8M18 3q5 7 0 14" fill="none" stroke="#3e5a98" stroke-width="1.5"/></svg>
  </div>
  <div class="contact">
    <b>Contact:</b> Lina Voss | Executive VP
    <b>O:</b> 8621 5550 1842
    <b>C:</b> 86 1550 010 2736
    <b>E:</b> lina.voss@amberlinepictures.com
  </div>
  <div class="rule"></div>
  <div class="copy">© 2014 Amberline Picture Works. All rights reserved.</div>
</footer>

</body>
</html>
```